Chiropractic Software Company needs Business Cards

We need a bushiness card design for use at a Chiropractic conference. We build billing, practice management, and medical documentation software. Our product is Halvern Chiropractic Software(Halvern for short). On top of our software we have practice success coaches that coordinate with our chiropractor clients to help them grow their practice and treat more patients. Our logo colors are tried-and-true orange-and-blue. We'd like a sterile white background and a clean layout; organizing the following information: Name, Position/Title, Phone Number, Address, email, and our website. On the backside we'd like our Logo and our slogan, "Your Practice Keystone" and our website(http://www.halvernchiropracticsoftware.example)

Industry/Entity Type

Business

```html
<!DOCTYPE html>
<html lang="en">
<head>
<meta charset="utf-8">
<title>Halvern Business Cards</title>
<link href="https://fonts.googleapis.com/css2?family=Open+Sans:ital,wght@0,400;0,600;0,700;1,400;1,700&display=swap" rel="stylesheet">
<style>
  :root {
    --page: #dcdcdc;
    --card-front: #ffffff;
    --card-back: #ececec;
    --blue: #29a3e0;
    --cyan: #5bbfd6;
    --green: #9cc23f;
    --orange: #d9703a;
    --yellow: #ebd77c;
    --ink: #3a3a3a;
    --ink-soft: #555555;
    --name-light: #8fd3f2;
    --brand: #2c7fc4;
    --brand-dot: #f07a24;
  }
  * { box-sizing: border-box; margin: 0; padding: 0; }
  html, body { width: 1200px; height: 1078px; overflow: hidden; }
  body {
    background: var(--page);
    font-family: "Open Sans", Arial, sans-serif;
    color: var(--ink);
    position: relative;
  }
  .card {
    position: absolute;
    left: 180px;
    width: 840px;
    height: 480px;
    overflow: hidden;
    box-shadow: 0 6px 18px rgba(0,0,0,0.18);
  }
  .card--front { top: 39px; background: linear-gradient(135deg, #ffffff 0%, #f3f3f3 100%); }
  .card--back { top: 559px; background: var(--card-back); }

  /* shared brand lockup */
  .brand { position: absolute; display: flex; align-items: center; gap: 14px; }
  .brand__dot { width: 50px; height: 50px; border-radius: 50%; background: var(--brand-dot); flex: none; }
  .brand__name { font-size: 38px; font-weight: 700; color: var(--brand); letter-spacing: 2px; line-height: 1; }

  /* front */
  .contact { position: absolute; left: 250px; top: 36px; font-size: 17px; line-height: 1.4; font-style: italic; }
  .contact__title, .social__title { font-weight: 700; letter-spacing: 0.5px; text-transform: uppercase; }
  .card--front .brand { left: 70px; top: 206px; }
  .social { position: absolute; right: 50px; top: 186px; text-align: right; font-size: 17px; line-height: 1.4; font-style: italic; }
  .person { position: absolute; right: 90px; top: 318px; text-align: right; }
  .person__name { font-size: 26px; font-weight: 700; text-transform: uppercase; letter-spacing: 0.5px; }
  .person__title { font-size: 17px; color: var(--ink-soft); text-transform: uppercase; }
  .stripe { position: absolute; left: 0; bottom: 28px; width: 100%; height: 30px; display: flex; }
  .stripe span { display: block; height: 100%; }
  .stripe .c, .stripe .g, .stripe .o, .stripe .y { width: 50px; }

  /* back */
  .card--back .brand { left: 70px; top: 46px; }
  .tagline { position: absolute; left: 70px; top: 116px; font-size: 24px; font-style: italic; color: var(--ink); }
  .back-site { position: absolute; left: 70px; top: 158px; font-size: 17px; color: var(--ink-soft); }
  .band { position: absolute; left: 0; top: 230px; width: 100%; height: 150px; display: flex; }
  .band span { display: block; height: 100%; }
  .band .c, .band .g, .band .o, .band .y { width: 55px; }
  .band .b { flex: 1; position: relative; }
  .band__role { position: absolute; right: 60px; top: 18px; font-size: 58px; font-weight: 700; color: #ffffff; letter-spacing: 1px; }
  .band__name { position: absolute; right: 62px; top: 92px; font-size: 30px; font-weight: 700; color: var(--name-light); }

  .c { background: var(--cyan); }
  .g { background: var(--green); }
  .o { background: var(--orange); }
  .y { background: var(--yellow); }
  .b { background: var(--blue); }
  .stripe .b { flex: 1; }
</style>
</head>
<body>
  <section class="card card--front" aria-label="Business card front">
    <div class="contact">
      <p class="contact__title">Contact us</p>
      <p>012 555 0148</p>
      <p>hello@halvern.example</p>
      <p>www.halvernchiropracticsoftware.example</p>
      <p>120 Calder Street, Suite 4, Brookfield</p>
    </div>
    <div class="brand">
      <div class="brand__dot"></div>
      <div class="brand__name">HALVERN</div>
    </div>
    <div class="social">
      <p class="social__title">Follow us on social</p>
      <p>connect.example/halvern</p>
      <p>updates.example/halvern</p>
      <p>portfolio.example/halvern</p>
    </div>
    <div class="person">
      <p class="person__name">Marcus Ellery</p>
      <p class="person__title">Founder</p>
    </div>
    <div class="stripe"><span class="c"></span><span class="g"></span><span class="o"></span><span class="y"></span><span class="b"></span></div>
  </section>

  <section class="card card--back" aria-label="Business card back">
    <div class="brand">
      <div class="brand__dot"></div>
      <div class="brand__name">HALVERN</div>
    </div>
    <p class="tagline">Your Practice Keystone</p>
    <p class="back-site">http://www.halvernchiropracticsoftware.example</p>
    <div class="band">
      <span class="c"></span><span class="g"></span><span class="o"></span><span class="y"></span>
      <span class="b">
        <span class="band__role">FOUNDER</span>
        <span class="band__name">Marcus Ellery</span>
      </span>
    </div>
  </section>
</body>
</html>
```